HRW / PFB

I need a business card for the owner of sister companies. Please see minimalist version of our old business card for just the Halvorsen business. We need to now have a card that shows off both the Halvorsen logo and the Pale Fern Builders logo. We would like the aesthetic to go well with our brand, and not differ greatly from our Halvorsen cards. These companies are sister companies, there is not one parent company. Looking for a visually appealing design, but not sure if it should be diagonal or something to make it visually attractive... or just some other type of divider. We prefer white logos with a blue background. White transparent background png logos are attached. Please use blue background with hex code 566b7c. The person and contact information will be on the back side, and I can do that myself. We will NOT need to add the text for design-build-sales-installation.

```html
<!DOCTYPE html>
<html lang="en">
<head>
<meta charset="utf-8">
<title>HRW / PFB Business Card</title>
<link rel="stylesheet" href="https://fonts.googleapis.com/css2?family=Montserrat:wght@400;600;700&display=swap">
<style>
  :root {
    --stage: #2f3133;
    --card-blue: #566b7c;
    --ink: #ffffff;
  }
  * { box-sizing: border-box; margin: 0; padding: 0; }
  html, body { width: 1200px; height: 694px; overflow: hidden; }
  body {
    background: var(--stage);
    font-family: "Montserrat", sans-serif;
    color: var(--ink);
    position: relative;
  }
  .card {
    position: absolute;
    top: 192px;
    width: 540px;
    height: 309px;
    background: var(--card-blue);
    border-radius: 18px;
    overflow: hidden;
  }
  .card--front { left: 40px; }
  .card--back { left: 620px; }

  /* stacked brand blocks: square above name */
  .brand {
    position: absolute;
    display: flex;
    flex-direction: column;
    font-weight: 600;
    line-height: 1.1;
    color: var(--ink);
    white-space: nowrap;
  }
  .brand__square { background: var(--ink); flex: none; }
  .brand__name span { display: block; }

  .divider { position: absolute; width: 1.5px; background: var(--ink); }

  /* front */
  .card--front .brand { top: 72px; width: 220px; align-items: center; text-align: center; gap: 14px; font-size: 20px; }
  .card--front .brand__square { width: 80px; height: 80px; }
  .card--front .brand--hrw { left: 30px; }
  .card--front .brand--pfb { left: 290px; }
  .card--front .divider { left: 269px; top: 70px; height: 170px; }

  /* back */
  .person { position: absolute; top: 38px; left: 120px; width: 260px; text-align: center; }
  .person__name { font-size: 22px; font-weight: 700; letter-spacing: 0.3px; }
  .person__role { font-size: 13px; font-weight: 400; margin-top: 2px; }

  .card--back .brand { font-size: 11px; gap: 6px; }
  .card--back .brand__square { width: 36px; height: 36px; }
  .card--back .brand--hrw { left: 26px; top: 100px; align-items: flex-start; }
  .card--back .brand--pfb { right: 26px; top: 22px; align-items: flex-end; text-align: right; }

  .contacts { position: absolute; list-style: none; font-size: 11px; font-weight: 400; }
  .contacts li { display: flex; align-items: center; gap: 7px; height: 17px; white-space: nowrap; }
  .contacts svg { width: 11px; height: 11px; flex: none; }
  .contacts--hrw { left: 26px; top: 184px; }
  .contacts--pfb { right: 26px; top: 96px; }
  .contacts--pfb li { justify-content: flex-end; }
  .card--back .divider { left: 300px; top: 110px; height: 95px; }

  .address {
    position: absolute; right: 26px; bottom: 24px;
    font-size: 11.5px; font-weight: 400; white-space: nowrap;
  }
</style>
</head>
<body>

<svg width="0" height="0" style="position:absolute">
  <defs>
    <symbol id="icon-mobile" viewBox="0 0 12 12"><rect x="3" y="0.8" width="6" height="10.4" rx="1.2" fill="none" stroke="#fff" stroke-width="1.1"/><line x1="5" y1="9.6" x2="7" y2="9.6" stroke="#fff" stroke-width="1"/></symbol>
    <symbol id="icon-phone" viewBox="0 0 12 12"><path d="M1 4.2c0-1.6 2.2-2.7 5-2.7s5 1.1 5 2.7v.8H8.6V3.8H3.4V5H1z" fill="#fff"/><path d="M2.6 6.2l1.4-1.4h4l1.4 1.4V11H2.6z" fill="#fff"/></symbol>
    <symbol id="icon-mail" viewBox="0 0 12 12"><rect x="0.8" y="2.4" width="10.4" height="7.2" fill="#fff"/><path d="M0.8 2.4L6 6.6l5.2-4.2" fill="none" stroke="#566b7c" stroke-width="1"/></symbol>
    <symbol id="icon-globe" viewBox="0 0 12 12"><circle cx="6" cy="6" r="5.2" fill="#fff"/><ellipse cx="6" cy="6" rx="2.2" ry="5.2" fill="none" stroke="#566b7c" stroke-width="0.8"/><line x1="0.8" y1="6" x2="11.2" y2="6" stroke="#566b7c" stroke-width="0.8"/></symbol>
  </defs>
</svg>

<section class="card card--front" aria-label="Card front">
  <div class="brand brand--hrw">
    <div class="brand__square"></div>
    <div class="brand__name"><span>Halvorsen</span><span>Kitchen + Bath</span></div>
  </div>
  <div class="divider"></div>
  <div class="brand brand--pfb">
    <div class="brand__square"></div>
    <div class="brand__name"><span>Pale Fern</span><span>Builders</span></div>
  </div>
</section>

<section class="card card--back" aria-label="Card back">
  <div class="person">
    <p class="person__name">Daniel Halvorsen</p>
    <p class="person__role">President / Owner</p>
  </div>

  <div class="brand brand--pfb">
    <div class="brand__square"></div>
    <div class="brand__name"><span>Pale Fern Builders</span></div>
  </div>
  <ul class="contacts contacts--pfb">
    <li>555-201-3386 <svg><use href="#icon-mobile"/></svg></li>
    <li>555-201-7730 <svg><use href="#icon-phone"/></svg></li>
    <li>daniel@palefernbuildersinc.com <svg><use href="#icon-mail"/></svg></li>
    <li>palefernbuildersinc.com <svg><use href="#icon-globe"/></svg></li>
  </ul>

  <div class="divider"></div>

  <div class="brand brand--hrw">
    <div class="brand__square"></div>
    <div class="brand__name"><span>Halvorsen</span><span>Kitchen + Bath</span></div>
  </div>
  <ul class="contacts contacts--hrw">
    <li><svg><use href="#icon-mobile"/></svg> 555-201-4417</li>
    <li><svg><use href="#icon-phone"/></svg> 555-201-7730</li>
    <li><svg><use href="#icon-mail"/></svg> daniel@halvorsenkitchenbath.com</li>
    <li><svg><use href="#icon-globe"/></svg> halvorsenkitchenbath.com</li>
  </ul>

  <p class="address">212 Orchard Lane, Brookhaven, MA 01999</p>
</section>

</body>
</html>
```